Real Estate Company / Capital Needs Cards!

need business cards designed using the logos that were just designed by sketchhive.

Reason: per designers request deadline extended 1 day…thank you.

Target Market(s)

Investors and clients looking to purchase real estate or invest in the business.

Industry/Entity Type

Business

Requirements
Must have
• two designs - one for the real estate logo and one for the capital logo, similar but slightly different.
Nice to have
• something to make it pop (perhaps on the back)
Should not have
• much color

```html
<!DOCTYPE html>
<html lang="en">
<head>
<meta charset="utf-8">
<title>Varden Real Estate – Business Cards</title>
<link rel="stylesheet" href="https://fonts.googleapis.com/css2?family=Crimson+Text:wght@400&display=swap">
<style>
  :root {
    --backdrop: #d3d3d3;
    --card: #0b0b0c;
    --mark: #8c8a86;
    --label: #a8a8a8;
    --name: #f2f2f2;
    --title: #bdbdbd;
    --detail: #8a8a8a;
  }
  * { margin: 0; padding: 0; box-sizing: border-box; }
  html, body {
    width: 1200px;
    height: 953px;
    overflow: hidden;
    background: var(--backdrop);
    font-family: "Crimson Text", "Times New Roman", serif;
  }
  .canvas { position: relative; width: 1200px; height: 953px; }
  .card {
    position: absolute;
    top: 257px;
    width: 244px;
    height: 440px;
    background: var(--card);
    overflow: hidden;
  }
  .card--front { left: 307px; }
  .card--back { left: 646px; text-align: center; }

  .brand {
    position: absolute;
    left: 0;
    right: 0;
    top: 178px;
    display: flex;
    justify-content: center;
    align-items: center;
    gap: 14px;
    color: var(--mark);
  }
  .brand__square { width: 48px; height: 48px; background: var(--mark); flex: none; }
  .brand__name {
    font-size: 20px;
    font-weight: 400;
    line-height: 24px;
    letter-spacing: 1px;
    white-space: nowrap;
  }

  .back__company {
    position: absolute; left: 0; right: 0; top: 74px;
    font-size: 15.5px; letter-spacing: 0.3px; color: var(--label);
  }
  .back__name {
    position: absolute; left: 0; right: 0; top: 154px;
    font-size: 23px; font-weight: 400; color: var(--name);
  }
  .back__role {
    position: absolute; left: 0; right: 0; top: 182px;
    font-size: 15.5px; color: var(--title);
  }
  .back__phone {
    position: absolute; left: 0; right: 0; top: 252px;
    font-size: 15px; color: var(--detail);
  }
  .back__address {
    position: absolute; left: 0; right: 0; top: 287px;
    font-size: 15.5px; line-height: 21px; color: var(--detail); font-style: normal;
  }
  .back__web {
    position: absolute; left: 0; right: 0; top: 372px;
    font-size: 15.5px; color: var(--detail);
  }
</style>
</head>
<body>
<main class="canvas">
  <section class="card card--front" aria-label="Card front">
    <div class="brand">
      <span class="brand__square"></span>
      <span class="brand__name">VARDEN<br>REAL ESTATE</span>
    </div>
  </section>

  <section class="card card--back" aria-label="Card back">
    <p class="back__company">VARDEN REAL ESTATE</p>
    <h1 class="back__name">Elena Varden</h1>
    <p class="back__role">CEO</p>
    <p class="back__phone">+1 555 014 2270</p>
    <address class="back__address">4210 Alder Lane<br>Westbury<br>Ohio 44090</address>
    <p class="back__web">vardenrealestate.com</p>
  </section>
</main>
</body>
</html>
```